Tarvell homes and renovations business card design.

Would like some new card designs utilizing my new logo that look professional. I am open to different colors on the logo or utilize the same ones we have. I like the original concept but would like to see some fresh ideas and build on what we have already done.

Target Market(s)

Custom home building industry, Real estate sales, Renovation projects.

Industry/Entity Type

Home Builder

Contact Information for Business Card

Tarvell Homes and Renovations
2871 162nd Street
Brackenford, Westmark
T0L3P0
Home : 403- 555-0187 Cell: 403- 555-0243

My info is : Gus Tarvell, President and CEO
email: tarvellhomes@quillmail.example
Website: tarvellhomes.example

Requirements
Must have
• Must Use my new logo design. I am open to different colors on the logo or utilize the same ones in the existing design. I can upload the original logo design if needed.

```html
<!DOCTYPE html>
<html lang="en">
<head>
<meta charset="utf-8">
<title>Tarvell Homes and Renovations – Business Card</title>
<link href="https://fonts.googleapis.com/css2?family=Open+Sans:wght@400;600;700&display=swap" rel="stylesheet">
<style>
  :root{
    --backdrop:#d9d9db;
    --card-black:#0b0b0c;
    --yellow:#fbbd23;
    --yellow-soft:#fcd46e;
    --cyan:#2bbfe6;
    --blue:#168cbe;
    --white:#ffffff;
    --ink:#1b1b1b;
  }
  *{box-sizing:border-box;margin:0;padding:0}
  html,body{width:1200px;height:960px;overflow:hidden}
  body{background:var(--backdrop);font-family:"Open Sans",Arial,sans-serif;position:relative}

  .card{position:absolute;top:180px;width:340px;height:595px;overflow:hidden;box-shadow:0 10px 30px rgba(0,0,0,.18)}
  .card--front{left:205px;background:var(--card-black)}
  .card--back{left:655px;background:var(--card-black)}

  /* front */
  .skyline-photo{position:absolute;inset:0 0 16px 0;
    background:linear-gradient(180deg,#0e0e10 0%,#1d1f23 45%,#232529 70%,#141517 100%)}
  .brand{position:absolute;left:0;right:0;text-align:center;color:var(--white);font-weight:700;font-size:21px;line-height:1.25;padding:0 30px}
  .brand__mark{display:inline-block;width:12px;height:12px;background:var(--yellow);margin-right:8px;vertical-align:middle}
  .card--front .brand{top:190px}
  .address{position:absolute;top:300px;left:0;right:0;text-align:center;color:var(--white);font-size:16px;line-height:1.45;letter-spacing:.5px}
  .phones{position:absolute;top:410px;left:0;right:0;text-align:center;color:var(--yellow);font-size:22px;line-height:1.5;letter-spacing:1px}
  .phones svg{width:14px;height:14px;vertical-align:middle;margin-right:6px;fill:var(--white)}
  .colour-bar{position:absolute;left:0;right:0;bottom:0;height:16px;display:flex}
  .colour-bar span{flex:1}

  /* back */
  .card--back .brand{top:170px}
  .band{position:absolute;left:0;right:0;display:flex;align-items:center;padding-left:28px}
  .band--name{top:345px;height:88px;background:var(--yellow);flex-direction:column;justify-content:center;align-items:center;padding:0}
  .band--email{top:437px;height:70px;background:var(--cyan)}
  .band--web{top:511px;height:66px;background:var(--blue)}
  .person__name{font-size:24px;font-weight:700;color:var(--ink)}
  .person__role{font-size:14px;font-weight:600;color:var(--white);letter-spacing:1px}
  .band__text{color:var(--white);font-size:15px;letter-spacing:.6px;white-space:nowrap}
  .band svg{width:16px;height:16px;margin-right:14px;fill:var(--white);flex:none}
</style>
</head>
<body>

<section class="card card--front">
  <div class="skyline-photo" role="img" aria-label="Dark, faded photograph of a city skyline with tall buildings"></div>
  <div class="brand"><span class="brand__mark"></span>Tarvell Homes and Renovations</div>
  <p class="address">2871 162nd Street<br>Brackenford, Westmark<br>T0L3P0</p>
  <div class="phones">
    <div><svg viewBox="0 0 24 24"><path d="M6.6 10.8a15.1 15.1 0 0 0 6.6 6.6l2.2-2.2a1 1 0 0 1 1-.25 11.4 11.4 0 0 0 3.6.57 1 1 0 0 1 1 1V20a1 1 0 0 1-1 1A17 17 0 0 1 3 4a1 1 0 0 1 1-1h3.5a1 1 0 0 1 1 1c0 1.250.2 2.45.57 3.57a1 1 0 0 1-.25 1z"/></svg>403- 555-0187</div>
    <div><svg viewBox="0 0 24 24"><path d="M6.6 10.8a15.1 15.1 0 0 0 6.6 6.6l2.2-2.2a1 1 0 0 1 1-.25 11.4 11.4 0 0 0 3.6.57 1 1 0 0 1 1 1V20a1 1 0 0 1-1 1A17 17 0 0 1 3 4a1 1 0 0 1 1-1h3.5a1 1 0 0 1 1 1c0 1.25.2 2.45.57 3.57a1 1 0 0 1-.25 1z"/></svg>403- 555-0243</div>
  </div>
  <div class="colour-bar">
    <span style="background:var(--yellow)"></span>
    <span style="background:var(--yellow-soft)"></span>
    <span style="background:var(--cyan)"></span>
    <span style="background:var(--blue)"></span>
  </div>
</section>

<section class="card card--back">
  <div class="brand"><span class="brand__mark"></span>Tarvell Homes and Renovations</div>
  <div class="band band--name">
    <div class="person__name">Gus Tarvell</div>
    <div class="person__role">President and CEO</div>
  </div>
  <div class="band band--email">
    <svg viewBox="0 0 24 24"><path d="M2 5h20v14H2z M3.5 6.5 12 13l8.5-6.5" fill="none" stroke="#fff" stroke-width="2"/></svg>
    <span class="band__text">tarvellhomes@quillmail.example</span>
  </div>
  <div class="band band--web">
    <svg viewBox="0 0 24 24"><circle cx="12" cy="12" r="9" fill="none" stroke="#fff" stroke-width="2"/><path d="M3 12h18M12 3c3 3 3 15 0 18M12 3c-3 3-3 15 0 18" fill="none" stroke="#fff" stroke-width="1.6"/></svg>
    <span class="band__text">www.tarvellhomes.example</span>
  </div>
</section>

</body>
</html>
```